Holiday Club Flyer for the Autumn half term school holidays for children aged 4 - 11 years old

Hi Please can someone adapt the attached flyer to reflect the new theme which is Deep Sea Divers. The dates need to be changed to 30th, 31st October and 1st November. Instead of saying mission can it say dive dates, dive location and dive times. Can you remove picnic lunch and just say lunch provided. Under the Dive times box instead of saying picnic lunch 12-12:30 can it just say collection @ 12:30.

Target Market(s)

Children aged between 4 - 11 years old

Requirements
Must have
• Eye catching and interesting for children, easy to read information and be bold.

```html
<!DOCTYPE html>
<html lang="en">
<head>
<meta charset="utf-8">
<title>Deep Sea Divers Holiday Club Flyer</title>
<link href="https://fonts.googleapis.com/css2?family=Poppins:wght@400;500;600;700&family=Lilita+One&family=Sniglet:wght@800&display=swap" rel="stylesheet">
<style>
:root{
  --bg:#dedede;
  --navy:#0b1a2e;
  --deep:#0d2a3f;
  --teal:#1e5a66;
  --orange:#f7931e;
  --lime:#a8d92b;
  --green:#4caf32;
  --box:rgba(22,80,150,.55);
  --box-line:#2f8fd8;
  --white:#ffffff;
  --pill:#e9541f;
}
*{box-sizing:border-box;margin:0;padding:0}
html,body{width:1200px;height:924px;overflow:hidden;background:var(--bg);font-family:"Poppins",sans-serif;color:var(--white)}
.page{position:absolute;top:130px;width:513px;height:664px;overflow:hidden;background:var(--navy)}
.page--info{left:70px}
.page--cover{left:618px}
.scene{position:absolute;inset:0}
.page--info .scene{background:
  radial-gradient(ellipse at 75% 55%,#3a4fa0 0%,rgba(58,79,160,0) 45%),
  radial-gradient(ellipse at 80% 85%,#7a5a3a 0%,rgba(122,90,58,0) 35%),
  linear-gradient(180deg,#123a55 0%,#0b1e33 45%,#091728 100%)}
.page--cover .scene{background:
  radial-gradient(ellipse at 50% 88%,#5a6b7a 0%,rgba(90,107,122,0) 30%),
  radial-gradient(ellipse at 15% 55%,#8a3a4a 0%,rgba(138,58,74,0) 30%),
  radial-gradient(ellipse at 88% 70%,#6a3a7a 0%,rgba(106,58,122,0) 30%),
  linear-gradient(180deg,#1f5a63 0%,#133c48 40%,#0c2332 100%)}
.abs{position:absolute}
.brand{left:34px;top:50px;display:flex;align-items:center;gap:10px}
.brand__dot{width:26px;height:26px;border-radius:50%;background:var(--green)}
.brand__name{font-weight:700;font-size:13px;color:var(--white)}
.club-title{left:150px;top:52px;font-weight:700;font-size:23px;line-height:20px;letter-spacing:.5px}
.free{left:240px;top:52px;width:42px;height:42px;border-radius:50%;background:var(--lime);color:#1a3a10;font-weight:700;font-size:12px;display:flex;align-items:center;justify-content:center;transform:rotate(-12deg)}
.age{left:287px;top:90px;width:80px;height:80px;border-radius:50%;background:var(--lime);color:#142a08;text-align:center;transform:rotate(-10deg);padding-top:12px;line-height:1}
.age__for{font-size:12px;font-weight:700}
.age__num{font-family:"Lilita One",sans-serif;font-size:28px}
.age__sub{font-size:8px;font-weight:700}
.label{left:35px;font-family:"Lilita One",sans-serif;line-height:.95}
.label__dive{display:block;font-size:28px;letter-spacing:1px}
.label__word{display:block;font-size:20px;color:var(--white);letter-spacing:.5px}
.label--orange .label__dive{color:var(--orange)}
.label--lime .label__dive{color:var(--lime)}
.info-box{left:113px;width:158px;border:1px solid var(--box-line);border-radius:3px;background:var(--box)}
.dates{top:125px;height:45px;display:flex}
.dates__day{flex:1;text-align:center;padding-top:6px;line-height:1.05;border-left:1px solid rgba(255,255,255,.35)}
.dates__day:first-child{border-left:0}
.dates__num{display:block;color:var(--orange);font-weight:700;font-size:12px}
.dates__mon{display:block;font-weight:600;font-size:15px}
.location{top:180px;height:45px;padding:8px 8px;font-size:11px;line-height:16px}
.location__name{color:var(--orange);font-weight:600}
.time{top:234px;height:47px;padding:9px 8px;font-size:8.5px;line-height:14px;font-weight:600}
.time__pill{display:inline-block;background:var(--pill);border-radius:8px;padding:0 5px;margin-left:4px}
.time__at{color:var(--lime)}
.features{left:33px;top:306px;width:270px;color:var(--lime);font-weight:700;font-size:15.5px;line-height:18px}
.bar{left:32px;width:238px;height:22px;display:flex;font-size:14px;font-weight:600}
.bar__lead{width:164px;background:linear-gradient(90deg,var(--green),#6cc23a);padding-left:8px;line-height:22px;border:1px solid #7ad040}
.bar__time{flex:1;background:var(--box);border:1px solid var(--box-line);line-height:20px;padding-left:5px}
.bar--drop{top:360px}
.bar--collect{top:387px}
.lunch{left:31px;top:416px;font-size:10.5px;letter-spacing:1.2px}
.register{left:33px;top:449px;font-family:"Lilita One",sans-serif;color:var(--orange);font-size:16px;letter-spacing:1px}
.url{left:33px;top:470px;font-weight:700;font-size:13.5px}
.divider{left:33px;top:500px;width:238px;border-top:1px dotted rgba(255,255,255,.55)}
.find{left:32px;top:513px;color:var(--lime);font-size:9.5px;font-weight:600}
.address{left:32px;top:526px;font-size:9.5px;font-weight:700;line-height:13px;text-transform:uppercase}
.email{left:32px;top:560px;font-size:10.5px;display:flex;align-items:center;gap:5px}
.cover-title{left:104px;top:92px;font-family:"Sniglet",sans-serif;font-weight:800;font-size:90px;line-height:74px;color:#f4f6f7}
.cover-title__line2{display:block;padding-left:2px}
</style>
</head>
<body>

<section class="page page--info">
  <div class="scene" role="img" aria-label="Underwater coral reef with tropical fish and a young girl in an orange dive mask and snorkel"></div>

  <div class="abs brand"><span class="brand__dot"></span><span class="brand__name">Tidepool Kids</span></div>
  <div class="abs club-title" style="left:150px;top:52px;display:none"></div>
  <div class="abs club-title" style="left:118px;top:74px">holiday<br>club</div>
  <div class="abs free" style="left:240px;top:52px">FREE!</div>

  <div class="abs age">
    <div class="age__for">FOR</div>
    <div class="age__num">4-11</div>
    <div class="age__sub">YEAR OLDS!</div>
  </div>

  <div class="abs label label--orange" style="top:124px"><span class="label__dive">DIVE</span><span class="label__word">DATES</span></div>
  <div class="abs info-box dates">
    <div class="dates__day"><span class="dates__num">30th</span><span class="dates__mon">Oct</span></div>
    <div class="dates__day"><span class="dates__num">31st</span><span class="dates__mon">Oct</span></div>
    <div class="dates__day"><span class="dates__num">1st</span><span class="dates__mon">Nov</span></div>
  </div>

  <div class="abs label label--lime" style="top:182px"><span class="label__dive">DIVE</span><span class="label__word" style="font-size:15px">LOCATION</span></div>
  <div class="abs info-box location">
    <div class="location__name">ST AIDAN'S CHURCH</div>
    <div>Millbrook Lane</div>
  </div>

  <div class="abs label label--orange" style="top:236px"><span class="label__dive">DIVE</span><span class="label__word">TIME</span></div>
  <div class="abs info-box time">
    <div>Drop-off, &amp; registration <span class="time__pill">08:45</span></div>
    <div>collection <span class="time__at">@12:30.</span></div>
  </div>

  <p class="abs features">Featuring games, bible stories, quizzes, craft &amp; more!</p>

  <div class="abs bar bar--drop"><span class="bar__lead">Drop off from</span><span class="bar__time">@8:45am</span></div>
  <div class="abs bar bar--collect"><span class="bar__lead">Collect your children</span><span class="bar__time">@12:30pm</span></div>
  <p class="abs lunch">(WITH A LUNCH PROVIDED FOR CHILDREN)</p>

  <p class="abs register">REGISTER AT</p>
  <p class="abs url">https://holidayclub.harbury.church</p>
  <div class="abs divider"></div>

  <p class="abs find">Find Us:</p>
  <p class="abs address">St Aidan's Church Harbury, Millbrook<br>Lane, Harbury, HB4 2QT</p>
  <p class="abs email">
    <svg width="12" height="9" viewBox="0 0 12 9" aria-hidden="true"><rect x=".5" y=".5" width="11" height="8" fill="none" stroke="#a8d92b"/><path d="M.5 .5 6 5l5.5-4.5" fill="none" stroke="#a8d92b"/></svg>
    holidayclub@harbury.church
  </p>
</section>

<section class="page page--cover">
  <div class="scene" role="img" aria-label="Underwater coral reef with tropical fish, a seahorse and a boy in a diving mask looking upward"></div>
  <h1 class="abs cover-title">Deep Sea<span class="cover-title__line2">Divers</span></h1>
</section>

</body>
</html>
```